National Training and assessment company needs a website

Create a 4 page website, simple but professional, the company provides training services to industry, resumes'/ CVs, personnel skill assessment, workplace skills profiling and develops manufactures and supplies training equipment for electrical/engineering training, Company title is Toren K Pty Ltd and also trades under BRW & Associates. letterheads etc all are done using dark green
Reason: Due to work commitments will be interstate from the 26/02 til 05/03/14
Target Market(s)
The market is broad covering the general public, secondary colleges and corporate sector
Industry/Entity Type
Training
Look and feel

```html
<!DOCTYPE html>
<html lang="en">
<head>
<meta charset="utf-8">
<title>Toren K Pty Ltd – BRW &amp; Associates</title>
<link href="https://fonts.googleapis.com/css2?family=Open+Sans:wght@400;600&display=swap" rel="stylesheet">
<style>
:root{
  --green:#1f7a1f;
  --green-dark:#0f5c12;
  --text:#333;
  --muted:#8a8a8a;
  --panel:#e4e4e4;
  --footer:#2b2b2b;
  --line:#c9c9c9;
}
*{box-sizing:border-box;margin:0;padding:0}
html,body{width:959px;height:1200px;overflow:hidden;background:#fff;font-family:"Open Sans",Arial,sans-serif;color:var(--text)}
.page{position:relative;width:959px;height:1200px}
.abs{position:absolute}

/* header */
.brand-sub{left:140px;top:8px;font-size:6px;color:var(--green)}
.brand-name{left:140px;top:18px;font-size:22px;line-height:26px;color:var(--green);font-weight:400;width:130px}
.brand-acn{left:140px;top:70px;font-size:5px;color:#444}
.login{left:522px;top:16px;font-size:10px;color:#444}
.phone{left:572px;top:13px;font-size:14px;color:var(--green);display:flex;align-items:center;gap:3px}
.social{left:693px;top:14px;display:flex;gap:4px}
.social span{width:18px;height:18px;border-radius:50%;background:#222;display:block}
.nav{left:353px;top:48px;display:flex;gap:0;font-size:11.5px}
.nav a{color:#333;text-decoration:none;padding:2px 7px;line-height:16px}
.nav a.active{background:var(--green);color:#fff;border-radius:5px;padding:2px 9px}

/* hero */
.hero{left:0;top:82px;width:959px;height:343px;background:linear-gradient(100deg,#b9cbd6 0%,#d8e1e6 40%,#9fb0b9 70%,#5d6c72 100%)}
.hero-box{left:137px;top:165px;width:479px;height:197px;background:rgba(90,95,100,.55);color:#fff;padding:8px 16px}
.hero-box h2{font-weight:400;font-size:18px;line-height:26px;letter-spacing:.2px}
.hero-box ul{list-style:none;margin-top:4px}
.hero-box li{font-size:16px;line-height:24px;display:flex;align-items:center;gap:12px;padding-left:9px}
.slider{left:164px;top:334px;width:122px;height:19px;background:#eee;border-radius:3px;display:flex;align-items:center;padding:0 6px;gap:5px}
.slider .dot{width:6px;height:6px;border-radius:50%;background:#aaa}
.slider .dot.on{background:#333}

/* welcome */
.welcome{left:0;top:425px;width:959px;height:119px;background:linear-gradient(#fafafa,#bdbdbd);text-align:center}
.welcome h1{font-size:18px;font-weight:600;color:#333;margin-top:8px}
.welcome p{font-size:11.5px;color:#888;line-height:19px;width:620px;margin:4px auto 0}
.btn{display:inline-block;margin-top:9px;background:var(--green);color:#fff;font-size:11px;font-weight:600;padding:6px 18px;border-radius:2px;border:1px solid var(--green-dark)}

/* features */
.feature{top:560px;width:190px;text-align:center}
.feature .art{width:90px;height:96px;margin:0 auto;background:linear-gradient(#e9e9e9,#d2d2d2);border-radius:4px}
.feature h3{font-size:11px;font-weight:600;color:var(--green);margin-top:10px}
.feature p{font-size:8px;color:var(--muted);line-height:14px;margin-top:4px}
.rule{left:137px;top:727px;width:687px;height:1px;background:var(--line)}

/* qualifications */
.quals{left:137px;top:750px;width:688px;height:184px;border:1px solid #ccc;background:linear-gradient(#fdfdfd,#d6d6d6);padding:10px 38px}
.quals h2{font-size:14px;font-weight:400;color:#333}
.quals ul{list-style:none;margin-top:4px}
.quals li{font-size:11px;line-height:23.4px;display:flex;align-items:center;gap:10px;padding-left:8px}
.quals .art{left:540px;top:4px;width:130px;height:176px;background:linear-gradient(#f4f4f4,#c9c9c9);border-radius:4px}

/* news */
.news-title{left:140px;top:958px;font-size:15px;color:#222}
.news-line{left:258px;top:969px;width:524px;height:1px;background:#999}
.news-nav{left:782px;top:960px;display:flex;gap:2px}
.news-nav span{width:18px;height:18px;background:#111;display:flex;align-items:center;justify-content:center}
.card{top:984px;width:222px;height:86px;background:var(--panel);border:1px solid #d5d5d5;display:flex}
.card .photo{width:92px;height:84px;background:linear-gradient(135deg,#c3c8cc,#6e7479)}
.card .body{padding:8px 7px 0 8px;flex:1;position:relative}
.card h4{font-size:11px;font-weight:400;color:#222}
.card p{font-size:7.5px;color:#777;line-height:12px;margin-top:4px;text-align:justify;font-family:Arial,sans-serif}
.card a{position:absolute;right:6px;bottom:4px;font-size:7.5px;color:var(--green);text-decoration:none;font-family:Arial,sans-serif}

/* footer */
.footer{left:0;top:1096px;width:959px;height:104px;background:var(--footer)}
.copy{left:134px;top:1137px;font-size:8.5px;color:#fff;font-family:Arial,sans-serif}
.foot-social{left:432px;top:1134px;display:flex;gap:2px}
.foot-social span{width:17px;height:17px;border-radius:2px;display:block}
.newsletter{left:656px;top:1134px;width:166px;height:20px;background:#fff;display:flex;align-items:center;justify-content:space-between;padding:0 6px 0 7px;font-size:8px;font-style:italic;color:#777;font-family:Arial,sans-serif}
</style>
</head>
<body>
<div class="page">

  <!-- header -->
  <div class="abs brand-sub">Toren K Pty Ltd T/As</div>
  <div class="abs brand-name">BRW &amp; Associates</div>
  <div class="abs brand-acn">ACN 000 000 000</div>

  <div class="abs login">LOG IN</div>
  <div class="abs phone">
    <svg width="8" height="12" viewBox="0 0 8 12"><path d="M3 0 L1 1 C0 3 0 8 2 11 L4 12 L5 9 L3.5 8 C3 6.5 3 5 3.5 3.5 L5 3 Z" fill="#555"/></svg>
    1-800-555-0199
  </div>
  <div class="abs social" aria-label="Social links">
    <span></span><span></span><span></span><span></span><span></span><span></span>
  </div>
  <nav class="abs nav">
    <a class="active" href="#">HOME</a>
    <a href="#">ABOUT US</a>
    <a href="#">SERVICE</a>
    <a href="#">MANAGEMENT</a>
    <a href="#">COURSE INFO</a>
    <a href="#">NEWS</a>
    <a href="#">CONTACT US</a>
  </nav>

  <!-- hero -->
  <div class="abs hero" role="img" aria-label="Photo of trainers and trainees working at computers in a bright office"></div>
  <div class="abs hero-box">
    <h2>DALE HAS MANY YEARS EXPERIENCE IN THE METALS<br>AND ENGINEERING SECTOR IN AREAS INCLUDING</h2>
    <ul>
      <li><svg width="12" height="12" viewBox="0 0 12 12"><circle cx="6" cy="6" r="6" fill="#fff"/><path d="M3 6.2 5.2 8.2 9 4" stroke="#666" stroke-width="1.8" fill="none"/></svg>Maintenance Engineering</li>
      <li><svg width="12" height="12" viewBox="0 0 12 12"><circle cx="6" cy="6" r="6" fill="#fff"/><path d="M3 6.2 5.2 8.2 9 4" stroke="#666" stroke-width="1.8" fill="none"/></svg>Control Systems</li>
      <li><svg width="12" height="12" viewBox="0 0 12 12"><circle cx="6" cy="6" r="6" fill="#fff"/><path d="M3 6.2 5.2 8.2 9 4" stroke="#666" stroke-width="1.8" fill="none"/></svg>Project management</li>
      <li><svg width="12" height="12" viewBox="0 0 12 12"><circle cx="6" cy="6" r="6" fill="#fff"/><path d="M3 6.2 5.2 8.2 9 4" stroke="#666" stroke-width="1.8" fill="none"/></svg>Management</li>
    </ul>
  </div>
  <div class="abs slider">
    <svg width="20" height="10" viewBox="0 0 20 10"><path d="M6 1 2 5 6 9" stroke="#111" stroke-width="2" fill="none"/><path d="M13 1 17 5 13 9" stroke="#777" stroke-width="1.5" fill="none"/></svg>
    <span class="dot"></span><span class="dot"></span><span class="dot on"></span><span class="dot"></span><span class="dot"></span><span class="dot"></span>
  </div>

  <!-- welcome -->
  <section class="abs welcome">
    <h1>WELCOME TO TOREN K PTY LTD</h1>
    <p>Toren K Pty Ltd is dedicated to providing quality customer focused service in all its ventures. Toren K core business is workplace training assessment with broader services which include:</p>
    <span class="btn">READ MORE</span>
  </section>

  <!-- features -->
  <div class="abs feature" style="left:160px">
    <div class="art" role="img" aria-label="Icon illustration of a figure carrying a rising arrow"></div>
    <h3>Employer Workplace skills profiling</h3>
    <p>To provide learning opportunities that engage employees at all levels in organizational develop-</p>
  </div>
  <div class="abs feature" style="left:384px">
    <div class="art" role="img" aria-label="Icon illustration of a figure assembling puzzle pieces"></div>
    <h3>Employee skills profiling</h3>
    <p>To empower employees to take ownership of their personal growth and development.</p>
  </div>
  <div class="abs feature" style="left:611px">
    <div class="art" role="img" aria-label="Icon illustration of a figure holding a team symbol"></div>
    <h3>Workplace training and Assessment</h3>
    <p>To create healthy, inclusion focused organizations that value all employees as individuals and team</p>
  </div>
  <div class="abs rule"></div>

  <!-- qualifications -->
  <section class="abs quals">
    <h2>Dale holds a number of Qualifications and Licenses including:</h2>
    <ul>
      <li><svg width="13" height="13" viewBox="0 0 12 12"><circle cx="6" cy="6" r="6" fill="#1f7a1f"/><path d="M3 6.2 5.2 8.2 9 4" stroke="#fff" stroke-width="1.8" fill="none"/></svg>Bachelor of Education</li>
      <li><svg width="13" height="13" viewBox="0 0 12 12"><circle cx="6" cy="6" r="6" fill="#1f7a1f"/><path d="M3 6.2 5.2 8.2 9 4" stroke="#fff" stroke-width="1.8" fill="none"/></svg>Diploma Technical Teaching</li>
      <li><svg width="13" height="13" viewBox="0 0 12 12"><circle cx="6" cy="6" r="6" fill="#1f7a1f"/><path d="M3 6.2 5.2 8.2 9 4" stroke="#fff" stroke-width="1.8" fill="none"/></svg>Certificate IV Workplace Training &amp; Assessment</li>
      <li><svg width="13" height="13" viewBox="0 0 12 12"><circle cx="6" cy="6" r="6" fill="#1f7a1f"/><path d="M3 6.2 5.2 8.2 9 4" stroke="#fff" stroke-width="1.8" fill="none"/></svg>Diploma Electrical Systems</li>
      <li><svg width="13" height="13" viewBox="0 0 12 12"><circle cx="6" cy="6" r="6" fill="#1f7a1f"/><path d="M3 6.2 5.2 8.2 9 4" stroke="#fff" stroke-width="1.8" fill="none"/></svg>Trade Certificate Electrical Fitter/Mechanic</li>
      <li><svg width="13" height="13" viewBox="0 0 12 12"><circle cx="6" cy="6" r="6" fill="#1f7a1f"/><path d="M3 6.2 5.2 8.2 9 4" stroke="#fff" stroke-width="1.8" fill="none"/></svg>Metal and Engineering Competency Standards Registered Assessor</li>
    </ul>
    <div class="abs art" role="img" aria-label="Photo of a cheering businesswoman sitting with a laptop"></div>
  </section>

  <!-- news -->
  <div class="abs news-title">Latest News</div>
  <div class="abs news-line"></div>
  <div class="abs news-nav">
    <span><svg width="8" height="10" viewBox="0 0 8 10"><path d="M6 1 2 5 6 9" stroke="#fff" stroke-width="1.5" fill="none"/></svg></span>
    <span><svg width="8" height="10" viewBox="0 0 8 10"><path d="M2 1 6 5 2 9" stroke="#fff" stroke-width="1.5" fill="none"/></svg></span>
  </div>

  <article class="abs card" style="left:135px">
    <div class="photo" role="img" aria-label="Photo of a team meeting around a table seen from above"></div>
    <div class="body"><h4>April 24th, 2013</h4><p>Mes cuml dia sed in lacus ut eniascet etor ingerto aliiqt es sitet amet eismod ictor ut</p><a href="#">Read More &gt;&gt;</a></div>
  </article>
  <article class="abs card" style="left:368px">
    <div class="photo" role="img" aria-label="Photo of a woman working with a touch display"></div>
    <div class="body"><h4>April 24th, 2013</h4><p>Mes cuml dia sed in lacus ut eniascet etor ingerto aliiqt es sitet amet eismod ictor ut</p><a href="#">Read More &gt;&gt;</a></div>
  </article>
  <article class="abs card" style="left:601px">
    <div class="photo" role="img" aria-label="Photo of a businessman looking through binoculars"></div>
    <div class="body"><h4>April 24th, 2013</h4><p>Mes cuml dia sed in lacus ut eniascet etor ingerto aliiqt es sitet amet eismod ictor ut</p><a href="#">Read More &gt;&gt;</a></div>
  </article>

  <!-- footer -->
  <footer class="abs footer"></footer>
  <div class="abs copy">Copyright © 2014. All rights reserved.</div>
  <div class="abs foot-social" aria-label="Social links">
    <span style="background:#d6492f"></span><span style="background:#3b5a9a"></span><span style="background:#2fa6dd"></span><span style="background:#c8202c"></span><span style="background:#f28a25"></span>
  </div>
  <div class="abs newsletter">NEWS LETTER
    <svg width="22" height="14" viewBox="0 0 22 14"><rect x="1" y="1" width="20" height="12" fill="#fff" stroke="#333" stroke-width="1.5"/><path d="M1 1 11 8 21 1" stroke="#333" stroke-width="1.5" fill="none"/></svg>
  </div>
</div>
</body>
</html>
```